DELMORAN Auto Battery

We need top of the line design for a new product that we are launching, Automotive Batteries.
We are an exporter of Auto Spare parts based in China, our new products will be launched in October 2012, the website is to be presented as B2B not B2C, we deal directly with Importers all around the world.
Our vision for the website is to be Clean, elegant, smart, warm, reflects confidence and trust..therefore, the choice of themes, colors, fonts and graphics should take into considerations all above.
Since there are hundreds of Battery types, specs, sizes, weight...etc, we will need a upload template that will enable us to upload, modify and manipulate the data of the batteries.
Car battery importers
Automotive

```html
<!DOCTYPE html>
<html lang="en">
<head>
<meta charset="utf-8">
<title>DELMORAN Auto Batteries</title>
<link href="https://fonts.googleapis.com/css2?family=PT+Sans:wght@400;700&family=Arimo:wght@400;700&family=Tinos&display=swap" rel="stylesheet">
<style>
:root{
  --page:#ebebeb;
  --brand:#3a9bd5;
  --ink:#333;
  --muted:#666;
  --navy:#1f3f8f;
  --navy-dark:#17317a;
  --cyan-top:#2bc0ee;
  --cyan-bot:#0b97d0;
  --panel:#fff;
  --line:#d4d4d4;
  --dark-top:#6b6b6b;
  --dark-bot:#1e1e1e;
  --arrow:#c8381e;
  --banner-left:#c4d6f7;
  --banner-right:#8ea8dc;
  --footer:#000;
}
*{box-sizing:border-box;margin:0;padding:0}
html,body{width:931px;height:1200px;overflow:hidden}
body{background:var(--page);font-family:Arimo,Arial,sans-serif;color:var(--ink);position:relative}
.abs{position:absolute}
.logo{left:24px;top:12px;font:700 33px/1 "PT Sans",sans-serif;color:var(--brand);letter-spacing:.5px}
.contact-now{right:12px;top:17px;font:400 19px/1 "PT Sans",sans-serif;color:#666}
.main-nav{top:68px;left:0;width:931px;font-size:11.5px;font-weight:700;color:#444}
.main-nav span{position:absolute;white-space:nowrap}
.main-nav span::before{content:"";display:inline-block;width:4px;height:4px;border-radius:50%;background:#4aa3d6;margin-right:8px;vertical-align:middle}
.search-bar{left:9px;top:93px;width:912px;height:54px;border-radius:4px;background:linear-gradient(var(--cyan-top),var(--cyan-bot));border:1px solid #0a86b9}
.search-bar label{position:absolute;top:20px;color:#fff;font-weight:700;font-size:12.5px}
.search-bar .field{position:absolute;top:15px;height:23px;background:#fff;border:1px solid #7cc;font-size:12px;color:#999;padding:4px 6px}
.search-btn{position:absolute;left:776px;top:15px;width:96px;height:24px;border-radius:3px;background:linear-gradient(#3a6fc4,#1d4898);border:1px solid #163b80;color:#fff;font-weight:700;font-size:12.5px;text-align:center;line-height:22px}
.side-head{left:9px;width:182px;height:38px;border-radius:4px;background:linear-gradient(var(--dark-top),var(--dark-bot));color:#fff;font:700 13px/38px "PT Sans",sans-serif;text-align:center}
.side-box{left:9px;width:182px;background:var(--panel);border:1px solid var(--line);border-radius:3px}
.cat-list{list-style:none;padding:4px 4px 0}
.cat-list li{height:29.4px;border-bottom:1px solid #ccc;font-size:11.5px;line-height:29px;padding-left:21px;position:relative}
.cat-list li:last-child{border-bottom:none}
.cat-list li::before{content:"";position:absolute;left:5px;top:11px;border:3.5px solid transparent;border-left:4px solid var(--arrow)}
.cat-list li:first-child span{border-bottom:1px solid #333}
.side-text{padding:13px 10px;font-size:11px;line-height:14.3px;color:var(--muted)}
.read-more{position:absolute;right:9px;width:73px;height:18px;border-radius:3px;background:linear-gradient(#666,#000);color:#fff;font-size:11px;font-weight:700;text-align:center;line-height:17px}
.tabs{left:201px;top:157px;width:717px;display:flex;gap:8px}
.tab{flex:1;height:35px;border-radius:4px;background:linear-gradient(#4c72c2,#1f3f8f);color:#fff;font-weight:700;font-size:13px;text-align:center;line-height:35px}
.banner{left:201px;top:201px;width:717px;height:276px;border:1px solid #9ab2e0;display:flex}
.banner-photo{width:359px;background:linear-gradient(135deg,var(--banner-left),#a9c0ee)}
.banner-copy{flex:1;background:linear-gradient(var(--banner-right),#99b0e0);padding:40px 0 0 33px;color:#fff;border-right:22px solid #a6bbe6}
.banner-copy h2{font:400 22px/1 "PT Sans",sans-serif;color:#10307a}
.banner-copy h1{font:400 33px/1 "PT Sans",sans-serif;margin:12px 0 15px}
.banner-copy p{font-size:12.5px;line-height:17px;width:300px}
.banner-btn{display:inline-block;margin-top:22px;width:124px;height:23px;border-radius:3px;background:linear-gradient(#5aaef2,#2c86e0);border:1px solid #2171c9;font-size:12px;font-weight:700;text-align:center;line-height:21px}
.product-grid{left:201px;width:717px;display:grid;grid-template-columns:repeat(4,167px);column-gap:16px}
.card{height:180px;background:var(--panel);border:1px solid var(--line);border-radius:3px;padding:8px 7px}
.card-photo{height:88px;border:1px solid #ddd;background:linear-gradient(#fff,#f1f1f1);display:flex;align-items:center;justify-content:center}
.card-photo div{width:88px;height:74px;background:linear-gradient(#b0232a 0 30%,#222 30%)}
.card h3{font-size:13px;color:var(--navy);margin:8px 0 3px 3px}
.card p{font-size:11.5px;color:var(--muted);font-weight:700;line-height:14px;margin-left:3px}
.card-actions{display:flex;gap:5px;margin-top:7px}
.card-actions span{flex:1;height:19px;border-radius:3px;background:linear-gradient(#3a62b5,#1a3b8a);color:#fff;font-size:11.5px;font-weight:700;text-align:center;line-height:19px}
.view-all{left:810px;top:884px;font-size:12.5px;font-weight:700;color:#222}
.testi-title{left:208px;top:906px;font:400 17px/1 Tinos,serif;color:#333}
.testimonials{left:203px;top:930px;width:715px;height:144px;background:var(--panel);border-radius:3px;border:1px solid #e2e2e2}
.quote{position:absolute;top:38px;width:270px}
.quote h4{font-size:13px;color:#555;margin-bottom:10px}
.quote p{font-size:11.5px;line-height:17.5px;color:var(--muted)}
.divider{position:absolute;left:353px;top:14px;width:1px;height:118px;background:#ccc}
.footer{left:0;top:1100px;width:931px;height:100px;background:var(--footer);color:#fff;font-size:11px}
.footer-nav span{position:absolute;top:14px}
.copyright{position:absolute;left:19px;top:40px}
.powered{position:absolute;right:16px;top:17px}
.powered u{text-decoration:underline}
</style>
</head>
<body>
<div class="abs logo">DELMORAN</div>
<div class="abs contact-now">Contact Now: 860 555 0142</div>

<nav class="abs main-nav">
  <span style="left:78px">Home</span><span style="left:168px">About Company</span><span style="left:318px">Our Products</span><span style="left:464px">Order Now</span><span style="left:594px">Reviews</span><span style="left:709px">FAQ</span><span style="left:793px">Contact</span>
</nav>

<form class="abs search-bar">
  <label style="left:28px">Category:</label><div class="field" style="left:96px;width:176px"></div>
  <label style="left:286px">Type:</label><div class="field" style="left:335px;width:176px"></div>
  <label style="left:525px">Price:</label><div class="field" style="left:574px;width:78px">min</div>
  <label style="left:658px;font-weight:400">to</label><div class="field" style="left:677px;width:78px">max</div>
  <div class="search-btn">Search</div>
</form>

<div class="abs side-head" style="top:157px">CATEGORIES</div>
<div class="abs side-box" style="top:199px;height:454px">
  <ul class="cat-list">
    <li><span>Product 1</span></li><li>Product 1</li><li>Product 1</li><li>Product 1</li><li>Product 1</li><li>Product 1</li><li>Product 1</li><li>Product 1</li><li>Product 1</li><li>Product 1</li><li>Product 1</li><li>Product 1</li><li>Product 1</li><li>Product 1</li><li>Product 1</li>
  </ul>
</div>

<div class="abs side-head" style="top:669px">ORDER NOW</div>
<div class="abs side-box" style="top:708px;height:154px">
  <p class="side-text">The only way to success is through the right path and that's what we provide you. None of the other companies has the result we do. what we provide you. None of the other companies has the result we do.</p>
  <div class="read-more" style="top:127px">read more</div>
</div>

<div class="abs side-head" style="top:874px">24/7 CUSTOMER SERVICES</div>
<div class="abs side-box" style="top:912px;height:163px">
  <p class="side-text">The only way to success is through the right path and that's what we provide you. None of the other companies has the result we do. The only way to success is through the right path and that's what we provide you...</p>
  <div class="read-more" style="top:136px">read more</div>
</div>

<div class="abs tabs"><div class="tab">Free Shipping</div><div class="tab">Door Delivery</div><div class="tab">Button 3</div><div class="tab">Button 4</div></div>

<section class="abs banner">
  <div class="banner-photo" role="img" aria-label="Photo of a large white and blue truck battery"></div>
  <div class="banner-copy">
    <h2>For Fast &amp; Best Perfomance</h2>
    <h1>Auto Batteries</h1>
    <p>The only way to success is through the right path and that's what we provide you. None of the other companies has the result we do.</p>
    <div class="banner-btn">View Products</div>
  </div>
</section>

<section class="abs product-grid" style="top:490px">
  <div class="card"><div class="card-photo" role="img" aria-label="Photo of a car battery"></div><h3>Product Name</h3><p>Model No:<br>Price:</p><div class="card-actions"><span>Details</span><span>Buy Now</span></div></div>
  <div class="card"><div class="card-photo" role="img" aria-label="Photo of a car battery"></div><h3>Product Name</h3><p>Model No:<br>Price:</p><div class="card-actions"><span>Details</span><span>Buy Now</span></div></div>
  <div class="card"><div class="card-photo" role="img" aria-label="Photo of a car battery"></div><h3>Product Name</h3><p>Model No:<br>Price:</p><div class="card-actions"><span>Details</span><span>Buy Now</span></div></div>
  <div class="card"><div class="card-photo" role="img" aria-label="Photo of a car battery"></div><h3>Product Name</h3><p>Model No:<br>Price:</p><div class="card-actions"><span>Details</span><span>Buy Now</span></div></div>
</section>
<section class="abs product-grid" style="top:691px">
  <div class="card"><div class="card-photo" role="img" aria-label="Photo of a car battery"></div><h3>Product Name</h3><p>Model No:<br>Price:</p><div class="card-actions"><span>Details</span><span>Buy Now</span></div></div>
  <div class="card"><div class="card-photo" role="img" aria-label="Photo of a car battery"></div><h3>Product Name</h3><p>Model No:<br>Price:</p><div class="card-actions"><span>Details</span><span>Buy Now</span></div></div>
  <div class="card"><div class="card-photo" role="img" aria-label="Photo of a car battery"></div><h3>Product Name</h3><p>Model No:<br>Price:</p><div class="card-actions"><span>Details</span><span>Buy Now</span></div></div>
  <div class="card"><div class="card-photo" role="img" aria-label="Photo of a car battery"></div><h3>Product Name</h3><p>Model No:<br>Price:</p><div class="card-actions"><span>Details</span><span>Buy Now</span></div></div>
</section>

<div class="abs view-all">&lt;&lt; View All &gt;&gt;</div>
<h2 class="abs testi-title">Testimonials</h2>
<section class="abs testimonials">
  <svg class="abs" style="left:9px;top:62px" width="14" height="20" viewBox="0 0 14 20"><path d="M11 2 3 10l8 8" fill="none" stroke="#bbb" stroke-width="3"/></svg>
  <div class="quote" style="left:33px"><h4>Mr.Harlow</h4><p>The only way to success is through the right path and that's what we provide you. None of the other companies has the result we do.</p></div>
  <div class="divider"></div>
  <div class="quote" style="left:384px"><h4>Mr.Harlow</h4><p>The only way to success is through the right path and that's what we provide you. None of the other companies has the result we do.</p></div>
  <svg class="abs" style="left:692px;top:62px" width="14" height="20" viewBox="0 0 14 20"><path d="M3 2l8 8-8 8" fill="none" stroke="#bbb" stroke-width="3"/></svg>
</section>

<footer class="abs footer">
  <div class="footer-nav"><span style="left:20px">Home</span><span style="left:87px">About Us</span><span style="left:174px">Services</span><span style="left:255px">Products</span><span style="left:346px">Offers</span><span style="left:416px">Contact Us</span></div>
  <div class="copyright">© Copyright 2012 DELMORAN. All rights reserved.</div>
  <div class="powered">Powered by: <u>Northgate Studio</u></div>
</footer>
</body>
</html>
```